Reed & Vale NC grand opening (for BILLBOARD)

Advertising the grand opening of our cannabis/hemp shop in NC. We will sell all things hemp (flower, cartridges, disposables, edibles, creams, lotions, pet products etc...)

Requirements
Must have
• include, open starting Aug 1, but grand opening Aug 15th.
Nice to have
• Difference slogan ideas "Save some cash, buy our grass" "Find your perfect high at Reed & Vale cannabis store" "Experience Nature's Gift: Reed & Vale Cannabis Store"

```html
<!DOCTYPE html>
<html lang="en">
<head>
<meta charset="utf-8">
<title>Reed &amp; Vale – Grand Opening Billboard</title>
<link rel="stylesheet" href="https://fonts.googleapis.com/css2?family=Poppins:wght@500;600;700;800&display=swap">
<style>
  :root {
    --bg-deep: #1f290d;
    --leaf-green: #6fbf3e;
    --leaf-mid: #4c8c26;
    --white: #ffffff;
    --rule: rgba(255, 255, 255, 0.6);
  }
  * { margin: 0; padding: 0; box-sizing: border-box; }
  html, body {
    width: 1200px; height: 456px; overflow: hidden;
    background: var(--bg-deep);
    font-family: "Poppins", sans-serif;
  }
  .billboard {
    position: relative;
    width: 1200px; height: 456px;
    background: var(--bg-deep);
    overflow: hidden;
  }
  .frame {
    position: absolute;
    left: 35px; top: 40px; right: 39px; bottom: 41px;
    border: 2px solid var(--white);
  }
  .foliage {
    position: absolute;
    pointer-events: none;
  }
  .foliage--bottom-left {
    left: -220px; bottom: -260px;
    width: 760px; height: 560px;
    background: radial-gradient(closest-side, rgba(111,191,62,0.9) 0%, rgba(76,140,38,0.6) 40%, rgba(61,107,28,0.25) 70%, rgba(31,41,13,0) 100%);
  }
  .foliage--top-right {
    right: -200px; top: -220px;
    width: 480px; height: 520px;
    background: radial-gradient(closest-side, rgba(111,191,62,0.85) 0%, rgba(76,140,38,0.55) 40%, rgba(61,107,28,0.2) 70%, rgba(31,41,13,0) 100%);
  }
  .brand {
    position: absolute;
    left: 112px; top: 150px;
    display: flex; align-items: center; gap: 16px;
  }
  .brand__dot {
    width: 24px; height: 24px;
    border-radius: 50%;
    background: var(--leaf-green);
  }
  .brand__name {
    font-weight: 600;
    font-size: 68px;
    line-height: 1;
    color: var(--white);
    letter-spacing: -1px;
  }
  .headline {
    position: absolute;
    left: 612px; top: 78px;
    color: var(--white);
    font-weight: 800;
    font-size: 57px;
    line-height: 61px;
    letter-spacing: 0.5px;
    text-transform: uppercase;
  }
  .headline__line { display: block; }
  .headline__accent { color: var(--leaf-green); }
  .store-name {
    position: absolute;
    left: 612px; top: 216px;
    padding-bottom: 6px;
    border-bottom: 1px solid var(--rule);
    font-weight: 600;
    font-size: 32px;
    line-height: 42px;
    color: var(--white);
    text-transform: uppercase;
    letter-spacing: 0.3px;
  }
  .dates {
    position: absolute;
    left: 612px; top: 278px;
    display: flex; gap: 14px; align-items: baseline;
    font-weight: 600;
    font-size: 22px;
    line-height: 30px;
    color: var(--white);
    text-transform: uppercase;
  }
  .dates__grand { color: var(--leaf-green); font-weight: 700; }
  .dates__sep { color: var(--rule); }
  .location {
    position: absolute;
    left: 600px; top: 400px;
    padding: 0 14px;
    background: var(--bg-deep);
    display: flex; align-items: center; gap: 10px;
    font-weight: 500;
    font-size: 21px;
    line-height: 30px;
    color: var(--white);
    text-transform: uppercase;
  }
  .location__pin { width: 20px; height: 26px; }
</style>
</head>
<body>
  <main class="billboard">
    <div class="foliage foliage--bottom-left" role="img" aria-label="Illustrated cannabis leaves rising from the lower left corner"></div>
    <div class="foliage foliage--top-right" role="img" aria-label="Illustrated cannabis leaves hanging from the upper right corner"></div>

    <div class="frame"></div>

    <div class="brand">
      <span class="brand__dot"></span>
      <span class="brand__name">Reed &amp; Vale</span>
    </div>

    <h1 class="headline">
      <span class="headline__line">Find your</span>
      <span class="headline__line"><span class="headline__accent">Perfect high</span> at</span>
    </h1>

    <p class="store-name">Reed &amp; Vale Cannabis Store</p>

    <p class="dates">
      <span class="dates__open">Open Aug 1</span>
      <span class="dates__sep">|</span>
      <span class="dates__grand">Grand Opening Aug 15</span>
    </p>

    <p class="location">
      <svg class="location__pin" viewBox="0 0 20 26" aria-hidden="true">
        <path d="M10 0C4.5 0 0 4.4 0 9.8 0 17 10 26 10 26s10-9 10-16.2C20 4.4 15.5 0 10 0z" fill="#6fbf3e"/>
        <circle cx="10" cy="9.8" r="3.8" fill="#1f290d"/>
      </svg>
      Off Exit 4B Birchfield Rd
    </p>
  </main>
</body>
</html>
```